Young, modern, highly skilled carpenter needs business card design

I need a business card design for my construction business. Its called 'Pellwright Construction Solutions'. Im looking for a ultra modern design that incorporates P C S, the first letters of the name with only a subtle reference to carpentry. The design should reflect my high quality work and eye for detail. i have also uploaded some exmaple designs i like.

Industry/Entity Type

Construction

Requirements
Must have
• Name of business, my name, mobile number, ABN number, email address
Nice to have
• A logo incorporating the name of the business

```html
<!DOCTYPE html>
<html lang="en">
<head>
<meta charset="utf-8">
<title>Pellwright Construction Solutions — Business Card</title>
<link rel="stylesheet" href="https://fonts.googleapis.com/css2?family=Open+Sans:wght@400;600;700&family=Tinos&display=swap">
<style>
  :root {
    --brand-yellow: #fcd000;
    --brand-black: #0b0b0b;
    --paper: #ffffff;
    --ink: #111111;
    --shadow: rgba(0, 0, 0, 0.5);
  }
  * { box-sizing: border-box; margin: 0; padding: 0; }
  html, body {
    width: 1200px; height: 901px; overflow: hidden;
    background: var(--paper);
    font-family: "Open Sans", Arial, sans-serif;
  }
  .sheet { position: relative; width: 1200px; height: 901px; }

  .card {
    position: absolute; overflow: hidden;
    box-shadow: 9px 9px 7px var(--shadow);
  }
  .card--front  { left: 71px;  top: 71px;  width: 498px; height: 275px; background: var(--brand-black); }
  .card--back   { left: 617px; top: 71px;  width: 498px; height: 273px; background: var(--brand-yellow); }
  .card--city-a { left: 71px;  top: 541px; width: 498px; height: 275px; background: var(--brand-yellow); }
  .card--city-b { left: 630px; top: 541px; width: 498px; height: 275px; background: var(--brand-yellow); }

  .side-label {
    position: absolute; top: 378px;
    font-family: "Tinos", "Times New Roman", serif;
    font-size: 20px; color: var(--ink);
  }
  .side-label--front { left: 93px; }
  .side-label--back  { left: 645px; }

  /* wordmark: plain square + name, one colour, one weight */
  .wordmark { position: absolute; display: flex; align-items: flex-start; gap: 12px; font-weight: 700; line-height: 1.05; }
  .wordmark__square { flex: none; background: currentColor; }
  .wordmark__name { display: block; }
  .wordmark__line--big { display: block; }
  .wordmark__line--small { display: block; }

  .card--front .wordmark { left: 155px; top: 74px; color: var(--brand-yellow); }
  .card--front .wordmark__square { width: 62px; height: 62px; }
  .card--front .wordmark__line--big { font-size: 34px; }
  .card--front .wordmark__line--small { font-size: 17px; margin-top: 6px; }

  .card--back .wordmark { left: 35px; top: 104px; color: var(--brand-black); }
  .card--back .wordmark__square { width: 44px; height: 44px; }
  .card--back .wordmark__line--big { font-size: 27px; }
  .card--back .wordmark__line--small { font-size: 13px; margin-top: 5px; }

  .card--city-a .wordmark { left: 28px; top: 22px; color: var(--brand-black); }
  .card--city-a .wordmark__square { width: 40px; height: 40px; }
  .card--city-a .wordmark__line--big { font-size: 24px; }
  .card--city-a .wordmark__line--small { font-size: 12.5px; margin-top: 4px; }

  .card--city-b .wordmark { left: 28px; top: 20px; color: var(--brand-black); flex-direction: column; gap: 10px; }
  .card--city-b .wordmark__square { width: 40px; height: 40px; }
  .card--city-b .wordmark__line--big { font-size: 15.5px; white-space: nowrap; }

  .divider { position: absolute; left: 271px; top: 40px; width: 1.5px; height: 214px; background: var(--brand-black); }

  .person { position: absolute; color: var(--brand-black); }
  .person__name { font-size: 15.5px; font-weight: 700; line-height: 1.2; }
  .person__role { font-size: 12.5px; font-weight: 400; line-height: 1.3; }
  .card--back .person { left: 311px; top: 26px; }
  .card--city-a .person, .card--city-b .person { left: 364px; top: 14px; }

  .contact { position: absolute; font-size: 12.5px; line-height: 17px; color: var(--brand-black); }
  .contact dl { display: grid; grid-template-columns: 62px auto; }
  .contact dt { font-weight: 700; }
  .card--back .address { left: 311px; top: 92px; }
  .card--back .numbers { left: 311px; top: 148px; }
  .card--back .numbers dl { grid-template-columns: 70px auto; }
  .card--back .numbers dt:first-child, .card--back .numbers dd:nth-of-type(1) { font-weight: 700; }
  .card--back .email { left: 311px; top: 228px; }

  .skyline {
    position: absolute; left: 0; right: 0; top: 100px; bottom: 0;
    background: linear-gradient(to bottom, var(--brand-yellow) 0%, var(--brand-black) 42%, var(--brand-black) 100%);
  }

  .card--city-a .contact { color: var(--paper); }
  .card--city-b .contact { color: var(--brand-yellow); }
  .contact--foot { top: 205px; }
  .contact--foot.address { left: 34px; }
  .contact--foot.numbers { left: 184px; }
  .contact--foot.numbers dl { grid-template-columns: 62px auto; }
  .contact--foot.web { left: 352px; }
  .contact--foot.web dl { grid-template-columns: 68px auto; }
  .contact--foot.web dt { font-weight: 400; }
</style>
</head>
<body>
<main class="sheet">

  <section class="card card--front" aria-label="Card front">
    <div class="wordmark">
      <span class="wordmark__square"></span>
      <span class="wordmark__name">
        <span class="wordmark__line--big">Pellwright</span>
        <span class="wordmark__line--small">Construction Solutions</span>
      </span>
    </div>
  </section>
  <p class="side-label side-label--front">Front</p>

  <section class="card card--back" aria-label="Card back">
    <div class="wordmark">
      <span class="wordmark__square"></span>
      <span class="wordmark__name">
        <span class="wordmark__line--big">Pellwright</span>
        <span class="wordmark__line--small">Construction Solutions</span>
      </span>
    </div>
    <div class="divider"></div>
    <div class="person">
      <p class="person__name">Dean O’ Malley</p>
      <p class="person__role">Contractor</p>
    </div>
    <address class="contact address" style="font-style:normal">
      2/4512 Harbour Street<br>Kellridge QLD 4000<br>Kellridge East QLD 4002
    </address>
    <div class="contact numbers">
      <dl>
        <dt>ABN No :</dt><dd>038217459</dd>
        <dt>Phone:</dt><dd>07 3118 2406</dd>
        <dt>Fax :</dt><dd>07 3118 2406</dd>
        <dt>Mobile :</dt><dd>946213078</dd>
      </dl>
    </div>
    <p class="contact email">dean@pcs.co.au</p>
  </section>
  <p class="side-label side-label--back">Back</p>

  <section class="card card--city-a" aria-label="Card, skyline version one">
    <div class="skyline" role="img" aria-label="Black city skyline silhouette rising from the bottom edge"></div>
    <div class="wordmark">
      <span class="wordmark__square"></span>
      <span class="wordmark__name">
        <span class="wordmark__line--big">Pellwright</span>
        <span class="wordmark__line--small">Construction Solutions</span>
      </span>
    </div>
    <div class="person">
      <p class="person__name">Dean O’ Malley</p>
      <p class="person__role">Contractor</p>
    </div>
    <address class="contact contact--foot address" style="font-style:normal">
      2/4512 Harbour Street<br>Kellridge QLD 4000<br>Kellridge East QLD 4002
    </address>
    <div class="contact contact--foot numbers">
      <dl>
        <dt>Phone:</dt><dd>07 3118 2406</dd>
        <dt>Fax :</dt><dd>07 3118 2406</dd>
        <dt>Mobile :</dt><dd>946213078</dd>
      </dl>
    </div>
    <div class="contact contact--foot web">
      <dl>
        <dt>ABN No :</dt><dd>038217459</dd>
      </dl>
      <p>dean@pcs.co.au</p>
      <p>www.pcs.co.in</p>
    </div>
  </section>

  <section class="card card--city-b" aria-label="Card, skyline version two">
    <div class="skyline" role="img" aria-label="Black city skyline silhouette rising from the bottom edge"></div>
    <div class="wordmark">
      <span class="wordmark__square"></span>
      <span class="wordmark__name">
        <span class="wordmark__line--big">Pellwright Construction Solutions</span>
      </span>
    </div>
    <div class="person">
      <p class="person__name">Dean O’ Malley</p>
      <p class="person__role">Contractor</p>
    </div>
    <address class="contact contact--foot address" style="font-style:normal">
      2/4512 Harbour Street<br>Kellridge QLD 4000<br>Kellridge East QLD 4002
    </address>
    <div class="contact contact--foot numbers">
      <dl>
        <dt>Phone:</dt><dd>07 3118 2406</dd>
        <dt>Fax :</dt><dd>07 3118 2406</dd>
        <dt>Mobile :</dt><dd>946213078</dd>
      </dl>
    </div>
    <div class="contact contact--foot web">
      <dl>
        <dt>ABN No :</dt><dd>038217459</dd>
      </dl>
      <p>dean@pcs.co.au</p>
      <p>www.pcs.co.in</p>
    </div>
  </section>

</main>
</body>
</html>
```